Website refresh for BriarlineTechnest.com

I need a new fresh website with all of the information contained in briarlinetechnest.com. The website needs to be built on the wix platform as it handles my booking, calendar and email marketing. The imperative pages are Home, About, Services, Clients and Testimonials. The other pages I can recreate based on the design chosen.

Industry/Entity Type

IT Services

Coding

Coded - Design and coding required

Number of Pages Required

5+ page

Font styles to use
Serif

Colors
00AB8E
00BBA5
67D7C9
C6EFE9
E9F9F6

Requirements
Must have
• I will need to be able to edit the document using the Wix WYSIWYG platform.
Nice to have
• See drumplot.com for a look and feel.
Should not have
• n/a

```html
<!DOCTYPE html>
<html lang="en">
<head>
<meta charset="utf-8">
<title>Briarline Technest — Managed IT Services</title>
<link href="https://fonts.googleapis.com/css2?family=Lora:wght@500;600;700&family=Open+Sans:wght@400;600;700&display=swap" rel="stylesheet">
<style>
:root{
  --green:#00AB8E;
  --teal:#00BBA5;
  --mint:#67D7C9;
  --pale:#C6EFE9;
  --wash:#E9F9F6;
  --ink:#1d1d1d;
  --text:#444;
  --muted:#777;
  --dark:#1b1b1b;
  --white:#fff;
}
*{box-sizing:border-box;margin:0;padding:0}
html,body{width:1200px;height:3220px;overflow:hidden}
body{font-family:"Open Sans",Arial,sans-serif;color:var(--text);background:var(--white);position:relative}
.serif{font-family:"Lora",Georgia,serif}
section,header,footer{position:absolute;left:0;width:1200px}

/* header */
.site-header{top:0;height:96px;background:var(--white);display:flex;align-items:center;padding:0 110px;justify-content:space-between;box-shadow:0 2px 8px rgba(0,0,0,.05)}
.brand{display:flex;align-items:center;gap:14px}
.brand-mark{width:40px;height:40px;background:var(--green);border-radius:4px}
.brand-name{font-family:"Lora",Georgia,serif;font-weight:700;font-size:24px;line-height:1.05;color:var(--green)}
.main-nav{display:flex;align-items:center;gap:10px}
.main-nav a{font-size:15px;color:var(--ink);text-decoration:none;padding:8px 16px;border-radius:4px}
.main-nav a.active{background:var(--green);color:var(--white)}
.main-nav .login{background:var(--green);color:var(--white);margin-left:20px;padding:9px 22px}

/* hero */
.hero{top:96px;height:604px;background:linear-gradient(90deg,#f3f4f4,#e7e9ea)}
.hero-photo{position:absolute;right:0;top:0;width:660px;height:604px;background:linear-gradient(135deg,#d9dcde,#aeb3b8 55%,#5a6068)}
.hero-copy{position:absolute;left:120px;top:190px;width:420px}
.hero-title{font-family:"Lora",Georgia,serif;font-weight:700;font-size:64px;line-height:1.1;color:var(--green)}
.hero-copy p{margin-top:24px;font-size:15px;line-height:1.6;color:var(--ink)}
.btn-dark{display:inline-block;margin-top:28px;background:var(--ink);color:var(--white);font-size:15px;font-weight:600;padding:12px 24px;border-radius:3px}

/* section heading */
.section-title{display:flex;align-items:center;gap:10px;font-family:"Lora",Georgia,serif;font-weight:700;font-size:48px;color:var(--ink)}
.section-title span{color:var(--green)}
.title-icon{width:40px;height:56px;background:linear-gradient(#6b6b6b,#2a2a2a);border-radius:4px}

/* services */
.services{top:720px;height:560px}
.services .section-title{position:absolute;left:0;right:0;top:50px;justify-content:center}
.arrow{position:absolute;width:36px;height:36px;border-radius:50%;background:var(--green);display:flex;align-items:center;justify-content:center}
.service-cards{position:absolute;top:130px;left:110px;display:flex;gap:40px}
.service-card{width:300px}
.service-photo{height:200px;border-radius:4px}
.service-head{display:flex;align-items:center;gap:12px;margin-top:18px}
.svc-icon{width:34px;height:34px;background:var(--green);border-radius:4px;display:flex;align-items:center;justify-content:center}
.service-head h3{font-family:"Lora",Georgia,serif;font-size:22px;font-weight:600;color:var(--green)}
.service-card p{margin-top:16px;font-size:14px;line-height:1.6;color:var(--text)}

/* about */
.about{top:1280px;height:560px}
.about .section-title{position:absolute;left:110px;top:30px}
.about-copy{position:absolute;left:120px;top:120px;width:440px;font-size:14px;line-height:1.65;color:var(--ink)}
.about-copy p+p{margin-top:18px}
.about-copy .btn-green{display:inline-block;margin-top:20px;background:var(--green);color:var(--white);font-weight:600;padding:10px 20px;border-radius:3px}
.about-photo{position:absolute;right:0;top:30px;width:600px;height:530px;background:linear-gradient(160deg,#c9ccd0,#8e949a 50%,#3f444a)}

/* clients */
.clients{top:1840px;height:260px;background:var(--green)}
.client-row{position:absolute;left:140px;top:65px;display:flex;gap:34px}
.client-box{width:160px;height:130px;background:var(--white);border-radius:6px;display:flex;align-items:center;justify-content:center;text-align:center;padding:10px;font-weight:700;font-size:16px;color:var(--ink)}
.clients .arrow{background:var(--ink);top:112px}

/* testimonials */
.testimonials{top:2100px;height:640px}
.testimonials .section-title{position:absolute;left:0;right:0;top:90px;justify-content:center}
.testi-row{position:absolute;top:180px;left:170px;display:flex;gap:30px}
.testi-card{width:270px;height:370px;background:var(--white);box-shadow:0 2px 14px rgba(0,0,0,.12);border-radius:4px;text-align:center;padding:24px 22px;position:relative;overflow:hidden}
.avatar{width:86px;height:86px;border-radius:50%;margin:0 auto;background:linear-gradient(#d8c3a8,#9b7f63)}
.testi-card h4{font-family:"Lora",Georgia,serif;font-size:24px;font-weight:700;color:var(--ink);margin-top:10px}
.testi-card p{font-size:13px;line-height:1.55;margin-top:12px;color:var(--ink)}
.stars{color:#f2b01e;font-size:18px;letter-spacing:2px;margin-top:12px}
.testi-card.featured::after{content:"";position:absolute;left:0;right:0;bottom:0;height:8px;background:var(--green)}
.dots{position:absolute;top:570px;left:0;right:0;display:flex;justify-content:center;gap:8px}
.dots i{width:20px;height:5px;background:var(--mint);border-radius:3px}
.dots i:first-child{background:var(--ink)}

/* footer */
.site-footer{top:2760px;height:460px;background:var(--dark);color:#ddd}
.foot-brand{position:absolute;left:110px;top:70px;width:240px}
.foot-brand .brand-name{font-size:22px}
.foot-brand p{font-size:14px;line-height:1.55;margin-top:24px;color:#eee}
.socials{display:flex;gap:14px;margin-top:30px}
.socials i{width:28px;height:28px;border-radius:50%;background:#ddd}
.socials i:first-child{background:var(--green)}
.foot-col{position:absolute;top:70px}
.foot-col h5{font-family:"Lora",Georgia,serif;font-size:20px;font-weight:700;color:var(--white);margin-bottom:22px}
.foot-col li{list-style:none;font-size:14px;margin-bottom:16px;color:#ddd}
.foot-col.links{left:450px}
.foot-col.contact{left:630px;width:280px}
.foot-col.other{left:955px}
.contact-item{display:flex;gap:16px;font-size:14px;line-height:1.5;margin-bottom:22px}
.contact-item svg{flex:none;margin-top:3px}
.copyright{position:absolute;left:0;right:0;bottom:0;height:50px;background:#111;color:#ddd;font-size:13px;display:flex;align-items:center;justify-content:center}
</style>
</head>
<body>

<header class="site-header">
  <div class="brand">
    <div class="brand-mark"></div>
    <div class="brand-name">Briarline<br>Technest</div>
  </div>
  <nav class="main-nav">
    <a class="active">Home</a><a>About</a><a>Services</a><a>Clients</a><a>Testimonials</a>
    <a class="login">Log In</a>
  </nav>
</header>

<section class="hero">
  <div class="hero-photo" role="img" aria-label="Technician working inside an open desktop computer case"></div>
  <div class="hero-copy">
    <h1 class="hero-title">Briarline<br>Technest</h1>
    <p>Briarline Technest is a Managed Service Provider for numerous small businesses in the Raleigh/Durham Triangle area.</p>
    <span class="btn-dark">Get Started</span>
  </div>
</section>

<section class="services">
  <h2 class="section-title"><span class="title-icon" role="img" aria-label="Person at a computer icon"></span>Our <span>Services</span></h2>
  <div class="arrow" style="left:55px;top:228px"><svg width="14" height="14" viewBox="0 0 14 14"><path d="M9 2 4 7l5 5" fill="none" stroke="#fff" stroke-width="2.4"/></svg></div>
  <div class="arrow" style="right:55px;top:228px"><svg width="14" height="14" viewBox="0 0 14 14"><path d="M5 2l5 5-5 5" fill="none" stroke="#fff" stroke-width="2.4"/></svg></div>
  <div class="service-cards">
    <article class="service-card">
      <div class="service-photo" role="img" aria-label="Hand touching glowing data screen" style="background:linear-gradient(135deg,#2a5a86,#163049)"></div>
      <div class="service-head"><span class="svc-icon"><svg width="18" height="18" viewBox="0 0 18 18"><ellipse cx="9" cy="4" rx="6" ry="2.5" fill="#fff"/><path d="M3 4v10c0 1.4 2.7 2.5 6 2.5s6-1.1 6-2.5V4" fill="none" stroke="#fff" stroke-width="1.6"/></svg></span><h3>Data Recovery</h3></div>
      <p>Lorem ipsum dolor sit amet, consectetur adipiscing elit, sed do eiusmod tempor incididunt ut labore et dolore magna aliqua.</p>
    </article>
    <article class="service-card">
      <div class="service-photo" role="img" aria-label="Support agent with headset at a desk" style="background:linear-gradient(135deg,#c9d3da,#7c8c98)"></div>
      <div class="service-head"><span class="svc-icon"><svg width="18" height="18" viewBox="0 0 18 18"><rect x="2" y="3" width="14" height="9" rx="1" fill="none" stroke="#fff" stroke-width="1.6"/><path d="M6 15h6" stroke="#fff" stroke-width="1.6"/></svg></span><h3>Remote Support</h3></div>
      <p>Lorem ipsum dolor sit amet, consectetur adipiscing elit, sed do eiusmod tempor incididunt ut labore et dolore magna aliqua.</p>
    </article>
    <article class="service-card">
      <div class="service-photo" role="img" aria-label="Digital security lock over a network" style="background:linear-gradient(135deg,#1e4e8c,#0b1f3d)"></div>
      <div class="service-head"><span class="svc-icon"><svg width="18" height="18" viewBox="0 0 18 18"><rect x="4" y="8" width="10" height="8" rx="1" fill="#fff"/><path d="M6 8V5.5a3 3 0 0 1 6 0V8" fill="none" stroke="#fff" stroke-width="1.6"/></svg></span><h3>Internet Security</h3></div>
      <p>Lorem ipsum dolor sit amet, consectetur adipiscing elit, sed do eiusmod tempor incididunt ut labore et dolore magna aliqua.</p>
    </article>
  </div>
</section>

<section class="about">
  <h2 class="section-title"><span class="title-icon" role="img" aria-label="Person at a computer icon"></span>About <span>Us</span></h2>
  <div class="about-copy">
    <p>Briarline Technest is family owned and operated in Raleigh, NC. Other companies may offer similar services, but ours are the highest quality at an affordable price. We provide Remote Managed Services for numerous small businesses in the local area.</p>
    <p>We also provide on-site computer (PC and Mac) Repair and IT Support to small business and residential customers for the Raleigh/Durham Triangle area. With over 20 years of experience, we've seen a lot of changes in the technology industry. The key is to adapt to those changes and continue to learn.</p>
    <span class="btn-green">Get Started</span>
  </div>
  <div class="about-photo" role="img" aria-label="Technician assembling computer hardware on a workbench"></div>
</section>

<section class="clients">
  <div class="arrow" style="left:60px"><svg width="14" height="14" viewBox="0 0 14 14"><path d="M9 2 4 7l5 5" fill="none" stroke="#fff" stroke-width="2.4"/></svg></div>
  <div class="arrow" style="right:60px"><svg width="14" height="14" viewBox="0 0 14 14"><path d="M5 2l5 5-5 5" fill="none" stroke="#fff" stroke-width="2.4"/></svg></div>
  <div class="client-row">
    <div class="client-box">Qorvane</div>
    <div class="client-box">Pinecrest Law</div>
    <div class="client-box">Delford Law Firm</div>
    <div class="client-box">Millbrook</div>
    <div class="client-box">Corrin Fab LLC</div>
  </div>
</section>

<section class="testimonials">
  <h2 class="section-title"><span class="title-icon" role="img" aria-label="Person at a computer icon"></span>Our <span>Testimonials</span></h2>
  <div class="testi-row">
    <article class="testi-card">
      <div class="avatar" role="img" aria-label="Portrait of client Marla K"></div>
      <h4>Marla K</h4>
      <p>Total complete confidence and trust - I have used their services for a number of years for all of my equipment. They are responsive, timely and clearly solve any problems with alternative solutions and identification of any risks.</p>
      <div class="stars">★★★★★</div>
    </article>
    <article class="testi-card featured">
      <div class="avatar" role="img" aria-label="Portrait of client Dennis H"></div>
      <h4>Dennis H</h4>
      <p>This letter is written in response to excellent service we received from Owen Halvorsen. Owen is the principal at Briarline Technest located in Raleigh, NC.</p>
      <div class="stars">★★★★★</div>
    </article>
    <article class="testi-card">
      <div class="avatar" role="img" aria-label="Portrait of client Carla T"></div>
      <h4>Carla T</h4>
      <p>Hi Owen, Thanks so much for taking care of my computer so quickly! I am so relieved to have it back. I don't know what I would do without you. Happy to refer you to everyone I know.</p>
      <div class="stars">★★★★★</div>
    </article>
  </div>
  <div class="dots"><i></i><i></i><i></i></div>
</section>

<footer class="site-footer">
  <div class="foot-brand">
    <div class="brand"><div class="brand-mark"></div><div class="brand-name">Briarline<br>Technest</div></div>
    <p>Briarline Technest is a Managed Service Provider for numerous small business in the Raleigh/Durham Triangle area.</p>
    <div class="socials" aria-label="Social links"><i></i><i></i><i></i><i></i><i></i></div>
  </div>
  <div class="foot-col links">
    <h5>Main Links</h5>
    <ul><li>Home</li><li>About</li><li>Services</li><li>Clients</li><li>Testimonials</li><li>Contact Us</li></ul>
  </div>
  <div class="foot-col contact">
    <h5>Contact Us</h5>
    <div class="contact-item"><svg width="16" height="18" viewBox="0 0 16 18"><path d="M8 17s6-6 6-10A6 6 0 0 0 2 7c0 4 6 10 6 10z" fill="none" stroke="#ddd" stroke-width="1.6"/><circle cx="8" cy="7" r="2" fill="#ddd"/></svg><span>Halvorsen Services LLC, dba Briarline Technest 4470 Kestrel Ridge Rd Ste 210 Raleigh, NC 27600</span></div>
    <div class="contact-item"><svg width="16" height="16" viewBox="0 0 16 16"><path d="M3 1h3l1.5 4-2 1.2a9 9 0 0 0 4.3 4.3l1.2-2L15 10v3a2 2 0 0 1-2 2A12 12 0 0 1 1 3a2 2 0 0 1 2-2z" fill="none" stroke="#ddd" stroke-width="1.4"/></svg><span>800-555-0147</span></div>
    <div class="contact-item"><svg width="16" height="16" viewBox="0 0 16 16"><circle cx="8" cy="8" r="6.5" fill="none" stroke="#ddd" stroke-width="1.4"/><circle cx="8" cy="8" r="2.5" fill="none" stroke="#ddd" stroke-width="1.4"/></svg><span>help@briarlinetechnest.com</span></div>
  </div>
  <div class="foot-col other">
    <h5>Other Links</h5>
    <ul><li>Help</li><li>Support</li><li>FAQs</li><li>Cookies Policy</li><li>Terms &amp; Conditions</li><li>Privacy Policy</li></ul>
  </div>
  <div class="copyright">Copyright © 2024 Briarline Technest. All rights reserved.</div>
</footer>

</body>
</html>
```